Dale Morrikan Plumbing and Heating

Need a card design for a plumbing and heating company that does service and repair, remodels, and plumbing in new construction. Please add following on back side of card; Boilers, Water heaters, Gas lines, Sump pumps, Toilet repairs, Faucet repairs, Pipe thawing, Radiant heating, New construction, Remodels.

Industry/Entity Type

Plumber

Contact Information for Business Card

Was thinking white gloss card with colored logo in middle or black glossy card with silver logo in middle. Just a thought but very open to other designs.

Requirements
Must have
• Need following on front of card;
• P(203) 321-8689
• C(203) 232-9069
• Dale Morrikan 275 Larkwell St West, Stamford, Ct 06214
• service@DrainHearth.example (plumbing in blue, heating in red)
• www.DrainHearth.example (plumbing in blue, heating in red)
• Fully Licensed and Insured
Nice to have
• Elegant design

```html
<!DOCTYPE html>
<html lang="en">
<head>
<meta charset="utf-8">
<title>Dale Morrikan Plumbing and Heating – Business Card</title>
<link href="https://fonts.googleapis.com/css2?family=Open+Sans:wght@400;600;700&display=swap" rel="stylesheet">
<style>
  :root {
    --bg: #e9e6e1;
    --card-black: #0c0c0d;
    --card-black-hi: #2a2a2c;
    --card-white: #ffffff;
    --brand-blue: #2e63c0;
    --brand-red: #d8283a;
    --silver: #c9ccd1;
    --ink: #1b1b1b;
    --rule: #e6e6e6;
  }
  * { box-sizing: border-box; margin: 0; padding: 0; }
  html, body { width: 1200px; height: 913px; overflow: hidden; }
  body {
    background: var(--bg);
    font-family: "Open Sans", Arial, sans-serif;
    position: relative;
  }
  .card {
    position: absolute;
    width: 540px;
    height: 309px;
    border-radius: 16px;
    overflow: hidden;
    box-shadow: 0 12px 28px rgba(0,0,0,.25);
  }

  /* ---------- Front ---------- */
  .card--front {
    left: 50px; top: 110px;
    background: linear-gradient(135deg, var(--card-black-hi) 0%, var(--card-black) 45%, #151516 100%);
    color: #fff;
  }
  .front__band { position: absolute; left: 0; right: 0; bottom: 0; height: 16px; display: flex; }
  .front__band .blue { flex: 0 0 58%; background: var(--brand-blue); }
  .front__band .red  { flex: 1; background: var(--brand-red); }

  .front__brand {
    position: absolute; left: 34px; top: 98px; width: 230px;
    display: flex; align-items: center; gap: 10px;
  }
  .brand-dot { flex: 0 0 18px; height: 18px; border-radius: 50%; }
  .card--front .brand-dot { background: var(--silver); }
  .brand-name { font-weight: 700; font-size: 17px; line-height: 1.2; text-transform: uppercase; letter-spacing: .5px; }
  .card--front .brand-name { color: var(--silver); }

  .front__person { position: absolute; right: 30px; top: 30px; text-align: right; }
  .person-name { font-weight: 700; font-size: 22px; letter-spacing: .5px; }
  .person-role { font-size: 11px; font-weight: 600; color: var(--brand-blue); letter-spacing: 1px; }

  .front__rule { position: absolute; right: 30px; top: 96px; width: 230px; height: 1px; background: var(--rule); }
  .front__divider { position: absolute; left: 34px; right: 30px; top: 222px; height: 1px; background: rgba(255,255,255,.7); }

  .front__contact { position: absolute; right: 30px; top: 108px; text-align: right; font-size: 12px; line-height: 1.45; }
  .front__contact .address { margin-bottom: 8px; }
  .contact-line { display: flex; justify-content: flex-end; align-items: center; gap: 6px; }
  .contact-line svg { width: 11px; height: 11px; flex: 0 0 11px; }
  .c-blue { color: #4d86e8; }
  .c-red { color: var(--brand-red); }

  .front__license { position: absolute; left: 34px; top: 236px; font-size: 14px; }

  /* ---------- Back ---------- */
  .card--back {
    left: 610px; top: 480px;
    background: var(--card-white);
    color: var(--ink);
  }
  .back__band { position: absolute; left: 0; right: 0; bottom: 0; height: 16px; display: flex; }
  .back__band .red  { flex: 0 0 58%; background: var(--brand-red); }
  .back__band .blue { flex: 1; background: var(--brand-blue); }

  .back__brand {
    position: absolute; right: 34px; top: 70px; width: 240px;
    display: flex; align-items: center; gap: 10px;
  }
  .card--back .brand-dot { background: var(--brand-blue); }
  .card--back .brand-name { color: var(--brand-blue); }

  .services { position: absolute; left: 34px; top: 120px; list-style: none; font-size: 13px; font-weight: 600; line-height: 1.25; }
  .services li { display: flex; align-items: center; gap: 7px; }
  .services li::before { content: ""; width: 8px; height: 8px; border-radius: 50%; background: var(--brand-blue); }
</style>
</head>
<body>

  <section class="card card--front" aria-label="Business card front">
    <div class="front__brand">
      <span class="brand-dot"></span>
      <span class="brand-name">Dale Morrikan Plumbing and Heating</span>
    </div>

    <div class="front__person">
      <div class="person-name">EVAN TOLLIVER</div>
      <div class="person-role">OWNER</div>
    </div>
    <div class="front__rule"></div>

    <div class="front__contact">
      <div class="address">Dale Morrikan 275 Larkwell<br>St West, Stamford, Ct 06214</div>
      <div class="contact-line">(203) 555-0147
        <svg viewBox="0 0 12 12"><path d="M2.5 1h2l1 3-1.3 1a6 6 0 0 0 2.8 2.8l1-1.3 3 1v2A1.5 1.5 0 0 1 9.5 11 8.5 8.5 0 0 1 1 2.5 1.5 1.5 0 0 1 2.5 1z" fill="#4d86e8"/></svg>
      </div>
      <div class="contact-line">(203) 555-0183
        <svg viewBox="0 0 12 12"><rect x="3" y="0.5" width="6" height="11" rx="1.2" fill="none" stroke="#4d86e8" stroke-width="1.2"/><circle cx="6" cy="9.5" r=".8" fill="#4d86e8"/></svg>
      </div>
      <div class="contact-line">service@<span class="c-blue">Drain</span><span class="c-red">Hearth</span>.example
        <svg viewBox="0 0 12 12"><rect x=".8" y="2.5" width="10.4" height="7" rx="1" fill="none" stroke="#4d86e8" stroke-width="1.2"/><path d="M1 3l5 4 5-4" fill="none" stroke="#4d86e8" stroke-width="1.2"/></svg>
      </div>
      <div class="contact-line">www.<span class="c-blue">Drain</span><span class="c-red">Hearth</span>.example
        <svg viewBox="0 0 12 12"><circle cx="6" cy="6" r="5" fill="none" stroke="#4d86e8" stroke-width="1.1"/><path d="M1 6h10M6 1c-2.5 3-2.5 7 0 10M6 1c2.5 3 2.5 7 0 10" fill="none" stroke="#4d86e8" stroke-width="1"/></svg>
      </div>
    </div>

    <div class="front__divider"></div>
    <div class="front__license">Fully Licensed and Insured</div>

    <div class="front__band"><span class="blue"></span><span class="red"></span></div>
  </section>

  <section class="card card--back" aria-label="Business card back">
    <div class="back__brand">
      <span class="brand-dot"></span>
      <span class="brand-name">Dale Morrikan Plumbing and Heating</span>
    </div>

    <ul class="services">
      <li>Boilers</li>
      <li>Water heaters</li>
      <li>Gas lines</li>
      <li>Sump pumps</li>
      <li>Toilet repairs</li>
      <li>Faucet repairs</li>
      <li>Pipe thawing</li>
      <li>Radiant heating</li>
      <li>New construction</li>
      <li>Remodels</li>
    </ul>

    <div class="back__band"><span class="red"></span><span class="blue"></span></div>
  </section>

</body>
</html>
```